New layout for printer ink webiste

We require fresh ,easy to navigate layout for our online shop, everything can be changed even the logo open to ideas, We are cut price printer cartridge retailer pos is price, quality and speed of delivery. Design is for magento store website www.quillmora.ie (landing page and product page).

Target Market(s)

printer owners

Industry/Entity Type

Printer

Number of Pages Required

2 page

Requirements
Must have
• clear pricing, and what we sell.
Nice to have
• must keep quick search menu, maybe different layout
Should not have
• too much going on

```html
<!DOCTYPE html>
<html lang="en">
<head>
<meta charset="utf-8">
<title>quillmora.ie – Printer Cartridges</title>
<link href="https://fonts.googleapis.com/css2?family=Arimo:wght@400;700&display=swap" rel="stylesheet">
<style>
:root{
  --orange:#ff9900;
  --orange-dark:#f08a00;
  --price-bg:#ffff99;
  --ink:#111111;
  --muted:#555555;
  --white:#ffffff;
  --footer:#000000;
  --field-border:#e0e0e0;
}
*{box-sizing:border-box;margin:0;padding:0}
html,body{width:720px;height:1200px;overflow:hidden;background:var(--white)}
body{font-family:"Arimo",Arial,sans-serif;color:var(--ink);position:relative}

.topbar{position:absolute;top:0;left:0;width:720px;height:26px}
.phone{position:absolute;left:12px;top:6px;font-size:12px;display:flex;align-items:center;gap:6px}
.account-links{position:absolute;right:12px;top:5px;font-size:13px;display:flex;gap:10px}

.brand{position:absolute;left:12px;top:28px;font-size:26px;font-weight:700;color:var(--orange);letter-spacing:-0.5px}

.search{position:absolute;left:163px;top:28px;width:413px;height:26px;border:2px solid var(--orange);display:flex}
.search-input{flex:1;background:var(--white)}
.search-button{width:72px;background:var(--orange);color:var(--white);font-size:15px;font-weight:700;display:flex;align-items:center;justify-content:center}

.cart{position:absolute;left:598px;top:22px;display:flex;align-items:center;gap:4px}
.cart-count{width:22px;height:22px;border-radius:50%;background:var(--orange);color:var(--white);font-size:13px;font-weight:700;display:flex;align-items:center;justify-content:center}

.filter-panel{position:absolute;left:12px;top:120px;width:216px;height:307px;background:var(--orange);border-radius:16px;padding:10px 24px}
.filter-title{text-align:center;font-size:16px;font-weight:700;color:var(--ink);margin-bottom:12px}
.filter-field{height:26px;background:var(--white);border-radius:8px;border:1px solid var(--field-border);font-size:9px;color:#aaa;padding:0 10px;display:flex;align-items:center;margin-bottom:30px}

.product-list{position:absolute;left:276px;top:120px;width:432px}
.product-row{position:relative;height:132px;margin-bottom:12px}
.product-image{position:absolute;left:0;top:16px;width:104px;height:88px;border-radius:4px;background:linear-gradient(135deg,#2b2b2b 0%,#2b2b2b 30%,#26a7d8 40%,#e02b8a 55%,#f5d200 72%,#2b2b2b 88%)}
.product-text{position:absolute;left:132px;top:16px;font-size:10px;line-height:24px;color:var(--ink)}
.price-box{position:absolute;right:0;top:0;width:132px;height:132px;background:var(--price-bg);display:flex;align-items:center;justify-content:center;font-size:40px;color:var(--ink)}

.site-footer{position:absolute;left:0;top:1032px;width:720px;height:168px;background:var(--footer);color:var(--white);font-size:8px}
.footer-col{position:absolute;top:12px;line-height:11px}
.footer-col h3{font-size:9px;font-weight:700;margin-bottom:14px}
.col-company{left:12px}
.col-orders{left:120px}
.col-payment{left:533px}
.payment-cards{display:flex;gap:5px;margin-top:4px}
.payment-card{width:28px;height:18px;background:#d9d9d9;border-radius:2px}
.trust-badge{margin-top:6px;width:104px;height:50px;background:#1d8a3a;border:2px solid #d9d9d9;border-radius:4px}
</style>
</head>
<body>

<header class="topbar">
  <div class="phone">
    <svg width="14" height="14" viewBox="0 0 24 24" aria-hidden="true"><path fill="#111" d="M6.6 10.8a15.1 15.1 0 0 0 6.6 6.6l2.2-2.2a1 1 0 0 1 1-.25 11.4 11.4 0 0 0 3.6.57 1 1 0 0 1 1 1V20a1 1 0 0 1-1 1A17 17 0 0 1 3 4a1 1 0 0 1 1-1h3.5a1 1 0 0 1 1 1c0 1.25.2 2.45.57 3.57a1 1 0 0 1-.25 1z"/></svg>
    <span>1890 402718</span>
  </div>
  <nav class="account-links"><span>Register</span><span>Login</span></nav>
</header>

<div class="brand">quillmora.ie</div>

<div class="search">
  <div class="search-input"></div>
  <div class="search-button">Search</div>
</div>

<div class="cart">
  <span class="cart-count">1</span>
  <svg width="52" height="40" viewBox="0 0 52 40" aria-label="Cart"><path d="M2 4h8l6 24h28l5-16H13" fill="none" stroke="#111" stroke-width="2.5" stroke-linejoin="round"/><circle cx="20" cy="34" r="3" fill="#111"/><circle cx="40" cy="34" r="3" fill="#111"/></svg>
</div>

<aside class="filter-panel">
  <h2 class="filter-title">Search Product</h2>
  <div class="filter-field">Type Of Cart Ridge</div>
  <div class="filter-field">Chose Your Brand</div>
  <div class="filter-field">Select Printer Series</div>
  <div class="filter-field">Select Cartridge</div>
</aside>

<main class="product-list">
  <article class="product-row"><div class="product-image" role="img" aria-label="Multipack of black, cyan, magenta and yellow ink cartridges"></div><div class="product-text">lorem ipsum dolor lal<br>lorem ipsum dolor lal<br>lorem ipsum dolor lal<br>lorem ipsum dolor lal</div><div class="price-box">$5</div></article>
  <article class="product-row"><div class="product-image" role="img" aria-label="Multipack of black, cyan, magenta and yellow ink cartridges"></div><div class="product-text">lorem ipsum dolor lal<br>lorem ipsum dolor lal<br>lorem ipsum dolor lal<br>lorem ipsum dolor lal</div><div class="price-box">$5</div></article>
  <article class="product-row"><div class="product-image" role="img" aria-label="Multipack of black, cyan, magenta and yellow ink cartridges"></div><div class="product-text">lorem ipsum dolor lal<br>lorem ipsum dolor lal<br>lorem ipsum dolor lal<br>lorem ipsum dolor lal</div><div class="price-box">$5</div></article>
  <article class="product-row"><div class="product-image" role="img" aria-label="Multipack of black, cyan, magenta and yellow ink cartridges"></div><div class="product-text">lorem ipsum dolor lal<br>lorem ipsum dolor lal<br>lorem ipsum dolor lal<br>lorem ipsum dolor lal</div><div class="price-box">$5</div></article>
  <article class="product-row"><div class="product-image" role="img" aria-label="Multipack of black, cyan, magenta and yellow ink cartridges"></div><div class="product-text">lorem ipsum dolor lal<br>lorem ipsum dolor lal<br>lorem ipsum dolor lal<br>lorem ipsum dolor lal</div><div class="price-box">$5</div></article>
  <article class="product-row"><div class="product-image" role="img" aria-label="Multipack of black, cyan, magenta and yellow ink cartridges"></div><div class="product-text">lorem ipsum dolor lal<br>lorem ipsum dolor lal<br>lorem ipsum dolor lal<br>lorem ipsum dolor lal</div><div class="price-box">$5</div></article>
</main>

<footer class="site-footer">
  <div class="footer-col col-company">
    <h3>OUR COMPANY</h3>
    About us<br>Contact Us<br>Help<br>FAQ<br>Terms and Conditions<br>Privacy Policy
  </div>
  <div class="footer-col col-orders">
    <h3>ORDERS</h3>
    Recycle<br>Shipping &amp; Returns<br>Ordering Info<br>Cookies<br>My Account
  </div>
  <div class="footer-col col-payment">
    <div>Payment Option</div>
    <div class="payment-cards"><span class="payment-card"></span><span class="payment-card"></span><span class="payment-card"></span><span class="payment-card"></span><span class="payment-card"></span></div>
    <div class="trust-badge"></div>
  </div>
</footer>

</body>
</html>
```